Property development business card design

New build residential property developers. I want a professional look but customer friendly so not too corporate. I'm not sure what logo will look best so open to designs with either. Thank you

Also i don't want both names on one card its 2 names for 2 different cards but with the same design.

Industry/Entity Type

Residential

Contact Information for Business Card

KRT Developments Ltd,
58 Fenwick Lane,
Elmbrook,
Norfolk,
CB7 2RW

Property Research Manager
Moira Tindell

Managing Director
Derek Ashworth

```html
<!DOCTYPE html>
<html lang="en">
<head>
<meta charset="UTF-8">
<title>KRT Developments – Business Card</title>
<link href="https://fonts.googleapis.com/css2?family=Open+Sans:wght@400;600;700&display=swap" rel="stylesheet">
<style>
  :root {
    --stage: #e4e4e4;
    --paper: #ffffff;
    --brand-blue: #1e78c8;
    --brand-blue-light: #5aa6e6;
    --steel-dark: #3a3a3a;
    --steel-mid: #4d4d4d;
    --steel-light: #5c5c5c;
    --wordmark-grey: #5a5a5a;
    --wordmark-silver: #d6d6d6;
    --text-light: #f2f2f2;
    --divider: #8a8a8a;
  }
  * { box-sizing: border-box; margin: 0; padding: 0; }
  html, body {
    width: 1200px; height: 900px; overflow: hidden;
    background: var(--stage);
    font-family: "Open Sans", Arial, sans-serif;
  }
  .canvas {
    width: 1200px; height: 900px;
    display: flex; align-items: center; justify-content: center; gap: 40px;
  }
  .card {
    width: 520px; height: 300px;
    border-radius: 24px;
    overflow: hidden;
    position: relative;
    box-shadow: 0 14px 28px rgba(0,0,0,0.18);
  }
  .steel-surface {
    background: radial-gradient(ellipse at 50% 40%, var(--steel-light), var(--steel-mid) 55%, var(--steel-dark));
  }

  /* Front card */
  .card-front { background: var(--paper); display: flex; flex-direction: column; }
  .front-brand {
    height: 168px;
    display: flex; align-items: center; justify-content: center; gap: 14px;
  }
  .brand-dot {
    width: 54px; height: 54px; border-radius: 50%;
    background: var(--brand-blue);
  }
  .wordmark {
    font-weight: 600; font-size: 26px; letter-spacing: 1.5px;
    text-transform: uppercase;
  }
  .front-brand .wordmark { color: var(--wordmark-grey); }
  .brand-stripe {
    height: 12px;
    background: linear-gradient(to bottom, var(--brand-blue-light) 0 3px, var(--brand-blue) 3px 9px, #cfcfcf 9px);
  }
  .front-details {
    flex: 1;
    display: flex; align-items: center;
    padding: 0 24px 0 26px;
  }
  .person {
    width: 196px; text-align: right; padding-right: 14px;
  }
  .person-name { color: var(--brand-blue); font-weight: 700; font-size: 16px; line-height: 1.2; }
  .person-role { color: var(--text-light); font-weight: 600; font-size: 12.5px; margin-top: 2px; white-space: nowrap; }
  .details-divider { width: 1px; height: 92px; background: var(--divider); }
  .contact-list { list-style: none; padding-left: 14px; }
  .contact-list li {
    display: flex; align-items: flex-start; gap: 7px;
    color: var(--text-light); font-size: 13.5px; line-height: 19px;
    white-space: nowrap;
  }
  .contact-icon { width: 13px; height: 13px; margin-top: 3px; flex-shrink: 0; }

  /* Back card */
  .card-back {
    display: flex; flex-direction: column; align-items: center; justify-content: center; gap: 18px;
  }
  .card-back .brand-dot {
    width: 110px; height: 110px;
    background: var(--brand-blue);
  }
  .card-back .wordmark { color: var(--wordmark-silver); font-size: 28px; }
</style>
</head>
<body>
<main class="canvas">

  <section class="card card-front" aria-label="Business card front">
    <div class="front-brand">
      <span class="brand-dot"></span>
      <span class="wordmark">KRT Developments</span>
    </div>
    <div class="brand-stripe"></div>
    <div class="front-details steel-surface" role="img" aria-label="Perforated dark metal texture panel with contact details">
      <div class="person">
        <p class="person-name">Moira Tindell</p>
        <p class="person-role">Property Research Manager</p>
      </div>
      <div class="details-divider"></div>
      <ul class="contact-list">
        <li>
          <svg class="contact-icon" viewBox="0 0 16 16"><path fill="#f2f2f2" d="M3.6 1.2 6 3.6 4.6 5.4c.9 2.2 3.7 5 6 6l1.8-1.4 2.4 2.4-1.8 2.4C7.7 14.6 1.4 8.3 1.2 3z"/></svg>
          <span>170 382 946</span>
        </li>
        <li>
          <svg class="contact-icon" viewBox="0 0 16 16"><g fill="none" stroke="#f2f2f2" stroke-width="1.4"><circle cx="8" cy="8" r="6.5"/><ellipse cx="8" cy="8" rx="3" ry="6.5"/><path d="M1.5 8h13"/></g></svg>
          <span>www.krtdevelopment.com</span>
        </li>
        <li>
          <svg class="contact-icon" viewBox="0 0 16 16"><g fill="none" stroke="#f2f2f2" stroke-width="1.4"><rect x="1.5" y="3.5" width="13" height="9" rx="1"/><path d="M1.5 4 8 9l6.5-5"/></g></svg>
          <span>info@krtdevelopment.com</span>
        </li>
        <li>
          <svg class="contact-icon" viewBox="0 0 16 16"><path fill="#f2f2f2" d="M8 1a5 5 0 0 0-5 5c0 3.6 5 9 5 9s5-5.4 5-9a5 5 0 0 0-5-5zm0 7a2 2 0 1 1 0-4 2 2 0 0 1 0 4z"/></svg>
          <span>58 Fenwick Lane, Elmbrook,<br>Norfolk, CB7 2RW</span>
        </li>
      </ul>
    </div>
  </section>

  <section class="card card-back steel-surface" role="img" aria-label="Business card back on perforated dark metal texture with company name">
    <span class="brand-dot"></span>
    <span class="wordmark">KRT Developments</span>
  </section>

</main>
</body>
</html>
```